Flyer for Septic Pump Out Company

Ridgeway Tank Clearing – Septic Pump Out Services in Shoalhaven, NSW

Contact Details:
- Website: [www.ridgewaytankclearing-example.com.au]
- Phone: 0491 273 615
- Email: info@ridgewaytankclearing-example.com
- NSW Plumbers Licence: 318046K

At Ridgeway Tank Clearing, we provide professional and reliable septic tank pump-out services in Shoalhaven, NSW. Our team of Vac-Tanker Operators and licensed plumbers ensures that each service call is handled with the highest level of expertise and care. We are available 24/7 to meet your needs.

Our Services Include:
- Septic tank pump-outs
- Grease trap maintenance
- Winery and brewery waste management
- Aerobic treatment units (ATUs)
- Portable toilet pump-outs
- Stormwater removal
- Blockage clearing

With two purpose-built 12,000-litre vacuum trucks, capable of pumping liquids and sludge from depths up to 8 metres, we can access most septic tanks and grease traps with ease. Our compact design and 50-metre hose ensure that no job is too difficult for us to handle.

Why Maintain Your Septic System?

1. Save Money:Regular pump-outs are far more cost-effective than repairing or replacing a damaged system.
2. Prevent Health Hazards: Properly maintained septic systems reduce environmental and health risks, preventing groundwater contamination and safeguarding drinking water.
3. Property Value: A well-maintained septic system preserves the value of your property and ensures no delays in potential sales.

Signs of a Failing Septic System:
- Sewage surfacing over the drainfield
- Lush, green growth or soggy areas over the drainfield
- Slow or backed-up drains, toilets, or sinks
- Foul sewage odours around your property
- Poor well water test results

If you notice any of these signs, call us for a thorough system assessment. We can diagnose and clear blockages, assess the health of your septic system, and provide expert advice on long-term solutions.

What to Do If You Have a Septic Problem:

- Contact Ridgeway Tank Clearing:We'll assess the issue and recommend a solution. In many cases, a thorough pump-out will resolve the problem.
- Schedule Regular Maintenance: We recommend pumping your septic tank regularly and are happy to schedule follow-ups as needed—every 3 years is typical.
- Conserve Water: If your system hasn’t completely failed, water-saving measures can help alleviate stress on the system in the short term.
- Fence Off Problem Areas: If effluent is surfacing, make sure to fence off the affected area to keep people and pets safe.

At Ridgeway Tank Clearing, we’re committed to delivering prompt, dependable service at competitive prices. Whether it’s a routine maintenance job or an emergency, our team is here to help.

```html
<!DOCTYPE html>
<html lang="en">
<head>
<meta charset="utf-8">
<title>Ridgeway Tank Clearing – Septic Pump Out Services Flyer</title>
<link href="https://fonts.googleapis.com/css2?family=Poppins:wght@400;500;600;700&family=Michroma&display=swap" rel="stylesheet">
<style>
:root{
  --navy:#1c2d9c;
  --blue:#1f4fae;
  --sky:#0f8fc9;
  --green:#1f7a2a;
  --leaf:#4a8c2a;
  --ink:#1b1b1b;
  --panel:#e9eaee;
  --white:#ffffff;
  --stage:#d6d8db;
}
*{box-sizing:border-box;margin:0;padding:0}
html,body{width:1200px;height:881px;overflow:hidden}
body{background:var(--stage);font-family:'Poppins',sans-serif;position:relative}
.page{position:absolute;top:88px;width:503px;height:651px;background:var(--white);overflow:hidden;box-shadow:0 6px 12px rgba(0,0,0,.18)}
.page--front{left:68px}
.page--back{left:628px}

/* header */
.brand{position:absolute;left:27px;top:24px;display:flex;align-items:center;gap:8px}
.brand__dot{width:26px;height:26px;border-radius:50%;background:var(--green)}
.brand__name{font-weight:700;font-size:17px;color:var(--green);line-height:1}
.licence{position:absolute;left:302px;top:22px;width:179px;height:18px;background:linear-gradient(90deg,var(--sky),var(--navy));color:var(--white);font-size:9px;line-height:18px;text-align:center;box-shadow:0 3px 4px rgba(0,0,0,.25)}
.licence b{font-weight:600;font-style:italic}

/* photo placeholders */
.photo{position:absolute;top:72px;height:234px}
.photo--truck{left:0;width:282px;background:linear-gradient(180deg,#1aa0d6 0%,#3b9ad0 45%,#4f9a32 60%,#3f8a25 100%)}
.photo--hose{left:0;width:251px;background:linear-gradient(180deg,#18a0d8 0%,#2c8fd0 25%,#5aa83a 45%,#3f8a25 100%)}

/* front hero */
.hero-title{position:absolute;left:282px;top:72px;width:221px;height:117px;background:linear-gradient(90deg,#1160b8,var(--navy));color:var(--white);padding:18px 0 0 22px}
.hero-title h1{font-weight:500;font-size:27px;line-height:32px}
.hero-title p{font-size:9.5px;margin-top:2px}
.hero-copy{position:absolute;left:282px;top:189px;width:221px;height:117px;background:var(--panel);padding:10px 20px 0 20px;color:var(--blue);font-weight:600;font-size:11px;line-height:15.3px;text-align:justify}
.intro{position:absolute;left:24px;top:320px;width:458px;font-size:10px;line-height:11.8px;color:var(--ink);text-align:justify}

.services{position:absolute;left:25px;top:391px;width:453px;height:193px;border:1px solid var(--sky);background:var(--panel);border-radius:2px}
.services__head{position:absolute;left:61px;top:380px;width:380px;height:21px;background:linear-gradient(180deg,#2b6bd0,var(--navy));color:var(--white);font-family:'Michroma',sans-serif;font-size:13px;letter-spacing:4px;text-align:center;line-height:21px;box-shadow:0 3px 4px rgba(0,0,0,.3)}
.service{position:absolute;display:flex;align-items:center;gap:9px;color:var(--blue);font-weight:600;font-size:11px;line-height:13px;height:28px}
.service svg{flex:none}

/* footer */
.footer{position:absolute;left:0;top:603px;width:503px;height:48px}
.footer__green{position:absolute;left:0;top:0;width:250px;height:48px;background:var(--leaf);clip-path:polygon(0 0,88% 0,100% 50%,92% 100%,0 100%)}
.footer__blue{position:absolute;left:230px;top:0;width:273px;height:48px;background:linear-gradient(90deg,#1f97d4,#1f62c0);clip-path:polygon(15% 0,100% 0,100% 100%,0 100%)}
.footer__links{position:absolute;left:26px;top:8px;color:var(--white);font-size:9px;line-height:16px}
.footer__links span{display:flex;align-items:center;gap:6px}
.footer__phone{position:absolute;left:265px;top:7px;display:flex;align-items:center;gap:8px;color:var(--white);font-weight:600;font-size:25px;line-height:34px}

/* back */
.back-panel{position:absolute;left:251px;top:72px;width:252px;height:234px;background:var(--panel);padding:10px 14px 0 14px}
.back-panel h2{color:var(--blue);font-weight:600;font-size:13.5px;line-height:15.5px}
.back-panel h3{color:var(--green);font-weight:600;font-size:13px;margin-top:9px}
.signs{list-style:none;margin-top:4px}
.signs li{position:relative;padding-left:12px;font-size:10px;line-height:11.5px;color:var(--ink);margin-bottom:3.4px}
.signs li svg{position:absolute;left:0;top:2px}
.back-panel .note{margin-top:8px;font-size:8px;line-height:9.7px;color:var(--blue);text-align:justify}

.infobox{position:absolute;top:338px;width:229px;height:247px;border:1px solid var(--navy);border-radius:2px;padding:14px 7px 0 7px}
.infobox--why{left:20px}
.infobox--todo{left:260px}
.infobox__head{position:absolute;top:-10px;height:20px;color:var(--white);font-weight:500;font-size:10px;line-height:20px;text-align:center;box-shadow:0 3px 4px rgba(0,0,0,.3)}
.infobox--why .infobox__head{left:8px;width:214px;background:var(--green)}
.infobox--todo .infobox__head{left:7px;width:214px;background:var(--navy)}
.infobox h4{color:var(--blue);font-weight:600;font-size:12px;line-height:14px;margin-top:2px}
.infobox--why p{font-size:10px;line-height:15px;color:var(--ink);text-align:justify;margin-bottom:6px}
.infobox--todo p{font-size:10px;line-height:11.8px;color:var(--ink);text-align:justify;margin-bottom:6px}
</style>
</head>
<body>

<section class="page page--front">
  <div class="brand"><span class="brand__dot"></span><span class="brand__name">Ridgeway Tank Clearing</span></div>
  <div class="licence">NSW Plumbers Licence: <b>318046K</b></div>

  <div class="photo photo--truck" role="img" aria-label="White vacuum tanker truck parked on green grass under a blue sky"></div>
  <div class="hero-title">
    <h1>Septic Pump<br>Out Services</h1>
    <p>in Shoalhaven, NSW</p>
  </div>
  <div class="hero-copy">With two purpose built 12,000 litre vacuum trucks, capable of pumping liquids and sludge from depths up to 8 metres, we can access most septic tanks and grease traps with ease.</div>

  <p class="intro">At Ridgeway Tank Clearing, we provide professional and reliable septic tank pump-out services in Shoalhaven, NSW. Our team of Vac-Tanker Operators and licensed plumbers ensures that each service call is handled with the highest level of expertise &amp; care. We are available 24/7 to meet your needs.</p>

  <div class="services"></div>
  <div class="services__head">OUR SERVICES INCLUDE:</div>

  <div class="service" style="left:62px;top:413px">
    <svg width="28" height="28" viewBox="0 0 28 28"><circle cx="14" cy="14" r="13" fill="#fff" stroke="#1f4fae" stroke-width="1.2"/><rect x="7" y="11" width="14" height="8" fill="none" stroke="#1f4fae" stroke-width="1.2"/><path d="M7 15h14" stroke="#1f4fae"/></svg>
    Septic tank pump-outs</div>
  <div class="service" style="left:62px;top:455px">
    <svg width="28" height="28" viewBox="0 0 28 28"><circle cx="14" cy="14" r="13" fill="#fff" stroke="#1f4fae" stroke-width="1.2"/><path d="M14 7c3 4 4 6 4 8a4 4 0 0 1-8 0c0-2 1-4 4-8z" fill="none" stroke="#1f4fae" stroke-width="1.2"/></svg>
    Grease trap maintenance</div>
  <div class="service" style="left:62px;top:499px">
    <svg width="28" height="28" viewBox="0 0 28 28"><circle cx="14" cy="14" r="13" fill="#fff" stroke="#1f4fae" stroke-width="1.2"/><rect x="10" y="9" width="8" height="11" rx="1" fill="none" stroke="#1f4fae" stroke-width="1.2"/></svg>
    <span>Winery and brewery<br>waste management</span></div>
  <div class="service" style="left:62px;top:541px">
    <svg width="28" height="28" viewBox="0 0 28 28"><circle cx="14" cy="14" r="13" fill="#fff" stroke="#1f4fae" stroke-width="1.2"/><path d="M8 14h12v5H8z M11 14V9h6v5" fill="none" stroke="#1f4fae" stroke-width="1.2"/></svg>
    Aerobic treatment units (ATUs)</div>

  <div class="service" style="left:261px;top:413px">
    <svg width="28" height="28" viewBox="0 0 28 28"><circle cx="14" cy="14" r="13" fill="#fff" stroke="#1f4fae" stroke-width="1.2"/><rect x="10" y="7" width="8" height="14" fill="none" stroke="#1f4fae" stroke-width="1.2"/><path d="M12 9v10" stroke="#1f4fae"/></svg>
    Portable toilet pump-outs</div>
  <div class="service" style="left:261px;top:455px">
    <svg width="28" height="28" viewBox="0 0 28 28"><circle cx="14" cy="14" r="13" fill="#fff" stroke="#1f4fae" stroke-width="1.2"/><path d="M9 16a3 3 0 0 1 2-5 4 4 0 0 1 7 1 2.5 2.5 0 0 1 1 4z" fill="none" stroke="#1f4fae" stroke-width="1.2"/></svg>
    Stormwater removal</div>
  <div class="service" style="left:261px;top:499px">
    <svg width="28" height="28" viewBox="0 0 28 28"><circle cx="14" cy="14" r="13" fill="#fff" stroke="#1f4fae" stroke-width="1.2"/><path d="M9 8v9a3 3 0 0 0 3 3h7" fill="none" stroke="#1f4fae" stroke-width="1.4"/></svg>
    Blockage clearing</div>

  <footer class="footer">
    <div class="footer__green"></div>
    <div class="footer__blue"></div>
    <div class="footer__links">
      <span><svg width="9" height="9" viewBox="0 0 10 10"><circle cx="5" cy="5" r="4.3" fill="none" stroke="#fff"/><path d="M1 5h8M5 1c-2 2.5-2 5.5 0 8M5 1c2 2.5 2 5.5 0 8" fill="none" stroke="#fff" stroke-width=".7"/></svg>ridgewaytankclearing-example.com.au</span>
      <span><svg width="9" height="9" viewBox="0 0 10 10"><circle cx="5" cy="5" r="5" fill="#fff"/><rect x="2.5" y="3.3" width="5" height="3.4" fill="none" stroke="#4a8c2a" stroke-width=".8"/></svg>info@ridgewaytankclearing-example.com</span>
    </div>
    <div class="footer__phone">
      <svg width="24" height="24" viewBox="0 0 24 24"><circle cx="12" cy="12" r="11" fill="#fff"/><path d="M8 6.5l2 .3.9 2.7-1.3 1a7 7 0 0 0 3.9 3.9l1-1.3 2.7.9.3 2c-.6 1.2-2 1.5-3 1.2A10 10 0 0 1 6.8 9.5c-.3-1 0-2.4 1.2-3z" fill="#1f62c0"/></svg>
      0491 273 615
    </div>
  </footer>
</section>

<section class="page page--back">
  <div class="brand"><span class="brand__dot"></span><span class="brand__name">Ridgeway Tank Clearing</span></div>
  <div class="licence">NSW Plumbers Licence: <b>318046K</b></div>

  <div class="photo photo--hose" role="img" aria-label="Operator in blue overalls and yellow gloves lowering a green suction hose into a septic tank opening on a lawn"></div>
  <div class="back-panel">
    <h2>Our compact design &amp; 50 metre hose ensure that no job is too difficult for us to handle.</h2>
    <h3>Signs of a Failing Septic System:</h3>
    <ul class="signs">
      <li><svg width="9" height="9" viewBox="0 0 9 9"><rect width="9" height="9" fill="#1f4fae"/><path d="M2 4.5l2 2 3-4" fill="none" stroke="#fff" stroke-width="1.2"/></svg>Sewage surfacing over the drainfield</li>
      <li><svg width="9" height="9" viewBox="0 0 9 9"><rect width="9" height="9" fill="#1f4fae"/><path d="M2 4.5l2 2 3-4" fill="none" stroke="#fff" stroke-width="1.2"/></svg>Lush, green growth or soggy areas over the drainfield</li>
      <li><svg width="9" height="9" viewBox="0 0 9 9"><rect width="9" height="9" fill="#1f4fae"/><path d="M2 4.5l2 2 3-4" fill="none" stroke="#fff" stroke-width="1.2"/></svg>Slow or backed-up drains, toilets, or sinks</li>
      <li><svg width="9" height="9" viewBox="0 0 9 9"><rect width="9" height="9" fill="#1f4fae"/><path d="M2 4.5l2 2 3-4" fill="none" stroke="#fff" stroke-width="1.2"/></svg>Foul sewage odours around your property</li>
      <li><svg width="9" height="9" viewBox="0 0 9 9"><rect width="9" height="9" fill="#1f4fae"/><path d="M2 4.5l2 2 3-4" fill="none" stroke="#fff" stroke-width="1.2"/></svg>Poor well water test results</li>
    </ul>
    <p class="note">If you notice any of these signs, call us for a thorough system assessment. We can diagnose and clear blockages, assess the health of your septic system, and provide expert advice on long-term solutions.</p>
  </div>

  <div class="infobox infobox--why">
    <div class="infobox__head">Why Maintain Your Septic System?</div>
    <h4>Save Money:</h4>
    <p>Regular pump-outs are far more cost effective than repairing or replacing a damaged system.</p>
    <h4>Prevent Health Hazards:</h4>
    <p>Properly maintained septic systems reduce environmental and health risks, preventing groundwater contamination &amp; safeguarding drinking water.</p>
    <h4>Property Value:</h4>
    <p>A well-maintained septic system preserves the value of your property and ensures no delays in potential sales.</p>
  </div>

  <div class="infobox infobox--todo">
    <div class="infobox__head">What to Do If You Have a Septic Problem:</div>
    <h4>Contact Ridgeway Tank Clearing:</h4>
    <p>We'll assess the issue and recommend a solution. In many cases, a thorough pump-out will resolve the problem.</p>
    <h4>Schedule Regular Maintenance:</h4>
    <p>We recommend pumping your septic tank regularly &amp; are happy to schedule follow ups as needed every 3 years is typical.</p>
    <h4>Conserve Water:</h4>
    <p>If your system hasn’t completely failed, water-saving measures can help alleviate stress on the system in the short term.</p>
    <h4>Fence Off Problem Areas:</h4>
    <p>If effluent is surfacing, make sure to fence off the affected area to keep people and pets safe.</p>
  </div>

  <footer class="footer">
    <div class="footer__green"></div>
    <div class="footer__blue"></div>
    <div class="footer__links">
      <span><svg width="9" height="9" viewBox="0 0 10 10"><circle cx="5" cy="5" r="4.3" fill="none" stroke="#fff"/><path d="M1 5h8M5 1c-2 2.5-2 5.5 0 8M5 1c2 2.5 2 5.5 0 8" fill="none" stroke="#fff" stroke-width=".7"/></svg>ridgewaytankclearing-example.com.au</span>
      <span><svg width="9" height="9" viewBox="0 0 10 10"><circle cx="5" cy="5" r="5" fill="#fff"/><rect x="2.5" y="3.3" width="5" height="3.4" fill="none" stroke="#4a8c2a" stroke-width=".8"/></svg>info@ridgewaytankclearing-example.com</span>
    </div>
    <div class="footer__phone">
      <svg width="24" height="24" viewBox="0 0 24 24"><circle cx="12" cy="12" r="11" fill="#fff"/><path d="M8 6.5l2 .3.9 2.7-1.3 1a7 7 0 0 0 3.9 3.9l1-1.3 2.7.9.3 2c-.6 1.2-2 1.5-3 1.2A10 10 0 0 1 6.8 9.5c-.3-1 0-2.4 1.2-3z" fill="#1f62c0"/></svg>
      0491 273 615
    </div>
  </footer>
</section>

</body>
</html>
```